Riverbend Haven Home Care-Nursing Assessment Form

I am creating a Nursing Assessment Form (which is used to be an intake form for all new patients) for my new home care company, Riverbend Haven Home Care.

It is 15 pages and pretty comprehensive as this is a very regulated field. I have all the necessary content and information attached in the word document below. Now, I am seeking a designer to make it look professional, cohesive and easy to read/ follow.
In order for your Word Document Design to be selected, you must:

1. As mentioned previously, make it easy to read/follow. There should be enough spacing, room to write out all necessary notes, fill out check marks...etc...
2. It should look professional.
3. It should be attractive and eye pleasing. Attached you will find our logo-kindly incorporate it's style into the project as well. The logo should be placed on top of each page.
4. Lastly, we need a Word Document version AND PDF Fillable Option. The fillable PDF should Auto Fill for the Name and Start of Care (SOC) Date.

I have attached a sample form below as well. This is how I envision the finished project to look. Of course, I am open to other suggestions as look as it meets the aforementioned requirements.

Thank you! May the best man or woman win!
Our team looks forward to working with our designer on this project!

Industry/Entity Type

Home Health Care

Font styles to use
Sans Serif

Colors
0255a3
9bcb3c

Requirements
Must have
• Refer to Project Description above.
Nice to have
We must be given a Word Document Option and PDF Fillable Option.

```html
<!DOCTYPE html>
<html lang="en">
<head>
<meta charset="utf-8">
<title>Riverbend Haven Home Care – Initial Assessment Form</title>
<link href="https://fonts.googleapis.com/css2?family=Roboto+Condensed:wght@400;700&family=Montserrat:wght@700&display=swap" rel="stylesheet">
<style>
:root{
  --brand-blue:#0255a3;
  --brand-green:#9bcb3c;
  --backdrop:#a9d6f7;
  --ink:#2e2e2e;
  --field-line:#a7d2ee;
  --field-fill:#fbfdff;
}
*{box-sizing:border-box;margin:0;padding:0}
html,body{width:857px;height:1200px;overflow:hidden;background:var(--backdrop)}
.canvas{position:relative;width:857px;height:1200px;overflow:hidden;font-family:"Roboto Condensed",sans-serif;color:var(--ink)}
.page{position:absolute;left:21px;top:24px;width:814px;height:1152px;background:linear-gradient(180deg,#fff 0%,#f6fbff 55%,#fff 100%)}
.brand{position:absolute;left:0;top:92px;width:857px;text-align:center}
.brand-name{font-family:"Montserrat",sans-serif;font-weight:700;font-size:17px;color:var(--brand-blue);letter-spacing:.2px}
.brand-dot{display:inline-block;width:14px;height:14px;border-radius:50%;background:var(--brand-green);vertical-align:-1px;margin-right:7px}
.title-band{position:absolute;left:0;top:164px}
.row{position:absolute;left:63px;width:732px;height:17px;display:flex;align-items:center;gap:6px;font-size:13.5px;line-height:17px;white-space:nowrap}
.row.tight{gap:4px;font-size:13px}
.field{flex:1;min-width:0;height:17px;border:1px solid var(--field-line);background:var(--field-fill)}
.box{flex:none;width:23px;height:17px;border:1px solid var(--field-line);background:var(--field-fill)}
.date-boxes{flex:none;display:flex;gap:3px}
.date-boxes .box{width:20px}
.heading{font-weight:700}
.gap{flex:none}
.spacer{flex:1}
.bullet{position:absolute;left:43px;top:328px;width:14px;height:14px;border-radius:50%;background:radial-gradient(circle at 35% 35%,#4aa3e8,var(--brand-blue))}
.footer-band{position:absolute;left:0;top:1166px}
</style>
</head>
<body>
<div class="canvas">
  <div class="page"></div>

  <header class="brand">
    <span class="brand-dot"></span><span class="brand-name">RIVERBEND HAVEN HOME CARE</span>
  </header>

  <svg class="title-band" width="857" height="20" viewBox="0 0 857 20" aria-label="Initial Assessment Form">
    <polygon points="21,0 137,0 130,18 21,18" fill="var(--brand-green)"/>
    <polygon points="152,0 712,0 702,18 146,18" fill="var(--brand-blue)"/>
    <polygon points="727,0 835,0 835,18 720,18" fill="var(--brand-green)"/>
    <text x="428" y="14" text-anchor="middle" fill="#fff" font-family="Roboto Condensed, sans-serif" font-weight="700" font-size="13" letter-spacing="4.5">INITIAL ASSESSMENT FORM</text>
  </svg>

  <div class="row" style="top:199px">Name <span class="field"></span>SOC Date <span class="date-boxes"><span class="box"></span><span class="box"></span><span class="box"></span><span class="box"></span><span class="box"></span><span class="box"></span></span></div>
  <div class="row" style="top:225px">Patient's Name <span class="field"></span>Gender <span class="field" style="flex:none;width:46px"></span>MR# <span class="field" style="flex:none;width:46px"></span>Date <span class="date-boxes"><span class="box"></span><span class="box"></span><span class="box"></span><span class="box"></span><span class="box"></span><span class="box"></span></span></div>
  <div class="row" style="top:249px">Primary Diagnosis <span class="field"></span>Secondary Diagnosis <span class="field"></span></div>
  <div class="row" style="top:275px">Other Pertinent Diagnosis <span class="field" style="flex:none;width:282px"></span>PCP Name <span class="field"></span></div>
  <div class="row" style="top:300px">Other Physician Name <span class="field"></span></div>
  <span class="bullet"></span>
  <div class="row" style="top:327px">Prognosis: <span class="gap" style="width:18px"></span>Poor <span class="box"></span><span class="gap" style="width:26px"></span>Fair <span class="box"></span><span class="gap" style="width:34px"></span>Good <span class="box"></span><span class="gap" style="width:34px"></span>Excellent <span class="box"></span><span class="spacer"></span></div>
  <div class="row" style="top:352px">Vital Signs: <span class="gap" style="width:12px"></span>Height <span class="field"></span>Weight <span class="field"></span>Temp <span class="field"></span>Pulse <span class="field"></span>Resp <span class="field"></span>B/P: <span class="field"></span></div>
  <div class="row" style="top:379px">Allergies: <span class="field"></span></div>
  <div class="row" style="top:404px">Past Medical and Surgical History <span class="field"></span></div>
  <div class="row" style="top:430px"><span class="field"></span></div>
  <div class="row heading" style="top:455px">Support System:</div>
  <div class="row" style="top:482px">Married <span class="box"></span><span class="gap" style="width:24px"></span>Not Married <span class="box"></span><span class="gap" style="width:28px"></span>Single <span class="box"></span><span class="gap" style="width:34px"></span>Divorced <span class="box"></span><span class="gap" style="width:34px"></span>Widowed <span class="box"></span><span class="spacer"></span></div>
  <div class="row" style="top:509px">Lives Alone: <span class="gap" style="width:22px"></span>Yes <span class="box"></span><span class="gap" style="width:36px"></span>No <span class="box"></span><span class="spacer"></span></div>
  <div class="row" style="top:534px">Family Composition: <span class="field"></span></div>
  <div class="row" style="top:561px">Legal Next of Kin: <span class="field"></span></div>
  <div class="row" style="top:587px">Address: <span class="field" style="flex:none;width:402px"></span>Email: <span class="field"></span></div>
  <div class="row" style="top:611px">Is significant other able, available, capable and</div>
  <div class="row" style="top:639px">willing to care for patient? <span class="gap" style="width:50px"></span>Yes <span class="box"></span><span class="gap" style="width:90px"></span>No <span class="box"></span><span class="spacer"></span><span class="field" style="flex:none;width:180px"></span><span class="gap" style="width:5px"></span></div>
  <div class="row" style="top:663px">If No, explain: <span class="field"></span></div>
  <div class="row" style="top:690px">Educational Needs of Patient/Family: <span class="field"></span></div>
  <div class="row" style="top:716px"><span class="field"></span></div>
  <div class="row heading" style="top:742px">Environment:</div>
  <div class="row" style="top:768px">Private Home <span class="box"></span>Apartment <span class="box"></span>Elevator <span class="box"></span>Walkup <span class="box"></span><span class="spacer"></span></div>
  <div class="row" style="top:792px"><span class="heading">Safety Hazards in the Home:</span> <span class="box"></span><span class="spacer"></span></div>
  <div class="row tight" style="top:817px">Sound Structure <span class="box"></span>Safe Placement of Cords, Rugs and Furniture <span class="box"></span>Adequate Heating and Ventilation <span class="box"></span>Adequate Cooking facility <span class="box"></span><span class="spacer"></span></div>
  <div class="row" style="top:846px">Adequate Plumbing/Sanitation/ Running Water <span class="box"></span>Adequate Sleeping Arrangement <span class="box"></span>Safe Gas/Electric Appliances <span class="box"></span><span class="spacer"></span></div>
  <div class="row" style="top:875px">Grounded Plug for Equipment <span class="box"></span>Enough Electrical Outlets for Equipment <span class="box"></span>Working Telephone in the Home <span class="box"></span><span class="spacer"></span></div>
  <div class="row tight" style="top:905px">Safe storage for Supplies/Equipment/Meds? <span class="box"></span>Exits Free of Obstruction <span class="box"></span>Working smoke detectors? <span class="box"></span>Fire extinguisher in home?<span class="spacer"></span></div>
  <div class="row" style="top:934px">Infestations of pests? <span class="box"></span>Neighborhood safe? <span class="box"></span><span class="spacer"></span></div>
  <div class="row" style="top:962px"><span class="heading">Comments:</span> <span class="field"></span></div>
  <div class="row heading" style="top:989px">Caregiver's Contact Information:</div>
  <div class="row" style="top:1012px">Name: <span class="field" style="flex:none;width:340px"></span>Telephone <span class="field"></span></div>
  <div class="row" style="top:1040px">Address: <span class="field" style="flex:none;width:415px"></span>Email: <span class="field"></span></div>
  <div class="row" style="top:1066px">Days /Time Available: <span class="field" style="flex:none;width:350px"></span><span class="spacer"></span></div>
  <div class="row heading" style="top:1095px">Caregivers Ability to Assist Patient / Able to Provide:</div>
  <div class="row" style="top:1119px">Personal Care: Yes <span class="box"></span>No <span class="box"></span>Mobility: Yes <span class="box"></span>No <span class="box"></span>Prepare/Serve Meals: Yes <span class="box"></span>No <span class="box"></span><span class="spacer"></span></div>
  <div class="row" style="top:1143px">Maintain Safe/Clean Environment Yes <span class="box"></span>No <span class="box"></span>Perform/ Assist with Procedures Yes <span class="box"></span>No <span class="box"></span><span class="spacer"></span></div>

  <svg class="footer-band" width="857" height="6" viewBox="0 0 857 6" aria-hidden="true">
    <rect x="21" y="0" width="240" height="6" fill="var(--brand-blue)"/>
    <polygon points="266,0 558,0 553,6 271,6" fill="var(--brand-green)"/>
    <rect x="563" y="0" width="272" height="6" fill="var(--brand-blue)"/>
  </svg>
</div>
</body>
</html>
```